Z Luxe Gel Top Coat & Base Coat Box Design

We are a wholesale nail and beauty supply company located in the USA. We need an attractive box design for our product, Z Luxe Gel Top Coat and Base Coat, to boost our sales to retail nail salons in the USA.
Dimension of the box is 11'' wide by 8.25'' long.
Color of the box is black with ingrained pattern (see picture).
Need design for top of box only.

Target Market(s)

Retail Nail Salons in the USA

Industry/Entity Type

Beauty Salon

Colors

Designer to choose colors to be used in the design.

Requirements
Must have
• Luxe Z Gel Top Coat Base Coat
• Matching Font of our product label (see picture)
Nice to have
• Premium should stand out.
• Line separating design for Top Coat and Base Coat (as they are 2 different products in the same box). Open to all color schemes, but would like to see some in silver.

```html
<!DOCTYPE html>
<html lang="en">
<head>
<meta charset="utf-8">
<title>Z Luxe Gel Top Coat &amp; Base Coat – Box Lid</title>
<link rel="stylesheet" href="https://fonts.googleapis.com/css2?family=Marcellus&display=swap">
<style>
  :root {
    --page: #f4f3f1;
    --lid: #2b221d;
    --lid-edge: #211a16;
    --silver: #d9d9db;
    --silver-soft: #a9a7a6;
    --ornament: #4a403a;
    --ornament-soft: #3b322d;
  }
  * { box-sizing: border-box; margin: 0; padding: 0; }
  html, body {
    width: 1200px;
    height: 1200px;
    overflow: hidden;
    background: var(--page);
  }
  .canvas {
    position: relative;
    width: 1200px;
    height: 1200px;
  }
  .lid {
    position: absolute;
    left: 60px;
    top: 195px;
    width: 1080px;
    height: 810px;
    background: var(--lid);
    box-shadow: inset 0 0 0 2px var(--lid-edge);
    font-family: "Marcellus", serif;
    color: var(--silver);
  }
  .lid-art {
    position: absolute;
    inset: 0;
    width: 1080px;
    height: 810px;
  }
  .monogram {
    position: absolute;
    left: 0;
    right: 0;
    top: 18px;
    text-align: center;
    font-size: 450px;
    line-height: 1;
    color: var(--silver);
  }
  .product-name {
    position: absolute;
    left: 0;
    right: 0;
    top: 500px;
    text-align: center;
    font-size: 62px;
    line-height: 1.25;
    letter-spacing: 1px;
  }
  .product-line {
    display: flex;
    justify-content: center;
    align-items: center;
    gap: 14px;
    margin-top: 8px;
    font-size: 66px;
  }
  .product-divider {
    display: inline-block;
    width: 3px;
    height: 66px;
    background: var(--silver);
  }
</style>
</head>
<body>
<main class="canvas">
  <section class="lid" aria-label="Box lid design">
    <svg class="lid-art" viewBox="0 0 1080 810" aria-hidden="false">
      <!-- frame -->
      <rect x="40" y="40" width="1000" height="730" fill="none" stroke="var(--silver-soft)" stroke-width="2.5"/>
      <rect x="48" y="48" width="984" height="714" fill="none" stroke="var(--silver-soft)" stroke-width="1"/>
      <!-- midpoint diamonds -->
      <g fill="var(--silver)">
        <path d="M540 32 l8 8 -8 8 -8 -8z"/>
        <path d="M540 762 l8 8 -8 8 -8 -8z"/>
        <path d="M32 405 l8 -8 8 8 -8 8z"/>
        <path d="M1032 405 l8 -8 8 8 -8 8z"/>
      </g>
      <!-- corner scroll areas -->
      <g role="img" aria-label="Silver scroll flourishes at the frame corners" fill="var(--ornament-soft)">
        <circle cx="52" cy="52" r="34"/>
        <circle cx="1028" cy="52" r="34"/>
        <circle cx="52" cy="758" r="34"/>
        <circle cx="1028" cy="758" r="34"/>
      </g>
      <!-- mandala ornament areas -->
      <g role="img" aria-label="Silver line mandala flower ornaments around the frame" fill="var(--ornament)">
        <ellipse cx="230" cy="50" rx="80" ry="42"/>
        <ellipse cx="850" cy="50" rx="80" ry="42"/>
        <ellipse cx="1030" cy="150" rx="48" ry="62"/>
        <ellipse cx="50" cy="170" rx="48" ry="62"/>
        <ellipse cx="50" cy="590" rx="48" ry="66"/>
        <ellipse cx="1030" cy="560" rx="48" ry="66"/>
        <ellipse cx="270" cy="740" rx="100" ry="48"/>
        <ellipse cx="810" cy="740" rx="100" ry="48"/>
      </g>
    </svg>

    <div class="monogram">Z</div>

    <h1 class="product-name">
      <span class="product-title">Luxe Z Gel</span>
      <span class="product-line">
        <span class="product-top">Top Coat</span>
        <span class="product-divider" aria-hidden="true"></span>
        <span class="product-base">Base Coat</span>
      </span>
    </h1>
  </section>
</main>
</body>
</html>
```